Poster/Handout for a dance

I need a poster designed that can also be made into a hand bill. Id like it to have an elegant feel - maybe black and gold

Wording: (feel free to tweak it)

Founders' Soiree
All adults and invited guests Join us for some R&R
an evening of music, dancing, relaxation, and appetizers and desserts
Friday, February 24 2017
8PM-11PM
North Birch Hall
4817 Maplebrook Cres NW

some ideas of looks below....

Font styles to use
Serif
Script

Colors
757575
000000

Requirements
Must have
• elegance....impact...professionalism
Should not have
• not too casual

```html
<!DOCTYPE html>
<html lang="en">
<head>
<meta charset="utf-8">
<title>Founders' Soiree — R&amp;R Evening</title>
<link href="https://fonts.googleapis.com/css2?family=Great+Vibes&family=Open+Sans:wght@500&family=Roboto+Condensed:wght@300;400&display=swap" rel="stylesheet">
<style>
  :root {
    --backdrop: #c9c9c9;
    --backdrop-edge: #757575;
    --ink: #000000;
    --cream: #f7efc9;
    --gold: #e9c25a;
    --gold-light: #fff4c2;
    --gold-deep: #a9802a;
    --white: #ffffff;
  }
  html, body {
    margin: 0;
    width: 1200px;
    height: 1200px;
    overflow: hidden;
  }
  body {
    background: radial-gradient(ellipse at center, #e4e4e4 0%, var(--backdrop) 55%, var(--backdrop-edge) 100%);
    position: relative;
    font-family: "Roboto Condensed", sans-serif;
  }
  .poster {
    position: absolute;
    left: 136px;
    top: 0;
    width: 928px;
    height: 1200px;
    background: var(--ink);
    overflow: hidden;
    color: var(--white);
  }
  .sparkle-field {
    position: absolute;
    left: 0; top: 0;
    width: 928px; height: 640px;
    background:
      radial-gradient(ellipse 60% 38% at 50% 0%, rgba(255,240,190,0.95) 0%, rgba(233,194,90,0.75) 30%, rgba(169,128,42,0.35) 60%, rgba(0,0,0,0) 100%),
      radial-gradient(ellipse 30% 50% at 10% 30%, rgba(233,194,90,0.45) 0%, rgba(0,0,0,0) 100%),
      radial-gradient(ellipse 30% 50% at 90% 30%, rgba(233,194,90,0.45) 0%, rgba(0,0,0,0) 100%),
      linear-gradient(180deg, rgba(169,128,42,0.5) 0%, rgba(0,0,0,0) 100%);
  }
  .title-ring {
    position: absolute;
    left: 284px; top: 39px;
    width: 360px; height: 360px;
    border-radius: 50%;
    background: var(--ink);
    border: 12px solid var(--gold);
    box-shadow: 0 0 0 4px var(--gold-deep), 0 0 40px rgba(255,220,130,0.8), inset 0 0 0 3px var(--gold-light);
  }
  .title-main {
    position: absolute;
    left: 0; width: 928px;
    top: 124px;
    text-align: center;
    font-size: 50px;
    color: var(--cream);
    line-height: 1;
  }
  .title-script {
    position: absolute;
    left: 0; width: 928px;
    top: 190px;
    text-align: center;
    font-family: "Great Vibes", cursive;
    font-size: 92px;
    color: var(--cream);
    line-height: 1;
  }
  .invite {
    position: absolute;
    left: 0; width: 928px;
    top: 497px;
    text-align: center;
    font-size: 37px;
    line-height: 50px;
    text-transform: uppercase;
  }
  .rr {
    position: absolute;
    left: 0; width: 928px;
    top: 582px;
    text-align: center;
    font-family: "Open Sans", sans-serif;
    font-weight: 500;
    font-size: 190px;
    line-height: 1;
    letter-spacing: -4px;
    background: linear-gradient(180deg, var(--white) 0%, var(--gold-light) 45%, var(--gold) 75%, var(--gold-deep) 100%);
    -webkit-background-clip: text;
    background-clip: text;
    color: transparent;
  }
  .glow-line {
    position: absolute;
    height: 3px;
    background: linear-gradient(90deg, rgba(233,194,90,0), var(--gold-light), rgba(233,194,90,0));
    box-shadow: 0 0 18px rgba(255,220,130,0.9);
  }
  .glow-line.under-rr { left: 230px; width: 468px; top: 744px; }
  .glow-line.band-top { left: 60px; width: 808px; top: 1017px; }
  .glow-line.band-bottom { left: 180px; width: 568px; top: 1152px; }
  .lead {
    position: absolute;
    left: 0; width: 928px;
    top: 769px;
    text-align: center;
    font-size: 35px;
    color: var(--cream);
  }
  .activities {
    position: absolute;
    left: 0; width: 928px;
    top: 813px;
    text-align: center;
    font-size: 27px;
    color: var(--cream);
  }
  .icon-row {
    position: absolute;
    left: 169px; top: 861px;
    display: flex;
    gap: 2px;
  }
  .icon-disc {
    width: 114px; height: 114px;
    border-radius: 50%;
    background: radial-gradient(circle at 40% 30%, var(--white) 0%, var(--gold-light) 35%, var(--gold) 85%, var(--gold-deep) 100%);
    box-shadow: 0 0 0 3px var(--ink);
  }
  .date {
    position: absolute;
    left: 76px; top: 1020px;
    font-size: 72px;
    font-weight: 300;
    color: var(--cream);
    line-height: 1.2;
    white-space: nowrap;
  }
  .details {
    position: absolute;
    left: 80px; top: 1103px;
    display: flex;
    align-items: baseline;
    color: var(--cream);
    white-space: nowrap;
  }
  .details .time { font-size: 37px; }
  .details .divider { font-size: 34px; margin: 0 26px 0 30px; }
  .details .venue { font-size: 25px; text-transform: uppercase; }
</style>
</head>
<body>
  <main class="poster">
    <div class="sparkle-field" role="img" aria-label="Gold glitter shower with falling stars and light rays"></div>
    <div class="title-ring"></div>
    <h1 class="title-main" style="margin:0;font-weight:400;">Founders'</h1>
    <div class="title-script">Soiree</div>

    <p class="invite" style="margin:0;">All adults and invited guests<br>Join us for some</p>
    <div class="rr">R&amp;R</div>
    <div class="glow-line under-rr"></div>

    <p class="lead" style="margin:0;">A lovely evening of</p>
    <p class="activities" style="margin:0;">Music, Dancing, Conversation, Fun, Relaxation, Appetizers, and Desserts</p>

    <div class="icon-row">
      <div class="icon-disc" role="img" aria-label="Music note icon"></div>
      <div class="icon-disc" role="img" aria-label="Dancer silhouette icon"></div>
      <div class="icon-disc" role="img" aria-label="Relaxation pose icon"></div>
      <div class="icon-disc" role="img" aria-label="Plate with spoon and fork icon"></div>
      <div class="icon-disc" role="img" aria-label="Cupcake dessert icon"></div>
    </div>

    <div class="glow-line band-top"></div>
    <div class="date">FRIDAY, FEBRUARY 24 2017</div>
    <div class="details">
      <span class="time">8PM-11PM</span>
      <span class="divider">|</span>
      <span class="venue">North Birch Hall 4817 Maplebrook Cres NW</span>
    </div>
    <div class="glow-line band-bottom"></div>
  </main>
</body>
</html>
```